Website for software company "velbra"

We need a website for our software company/startup named "velbra". We are developing several products (currently 3 standard-software products) which are all in different sectors, but all our products are available for Laptops/PC/Mobile Phones/Tablets, ... We do also create custom software and support our customers with consulting to optimize their processes.
We already have a Logo which you can find in the attached files.
We are a young team of 4 members (two founders and 2 employees).

To get an idea of our products -> the first one is a planning software for healthcare organizations (eg. Mercyway, firebrigade, pharmacy), the second one is a booking software for sport clubs and the third one is a competition software for sports hunting. You see very diverse. Include or ignore this info of our products as you like.

The design has to be a bootstrap 4 (or higher) design. We have licenced FontAwesome as iconset. Responsive design should come without saying.

Coding

Coded - Design and coding required

Number of Pages Required

5+ page

Font styles to use
Sans Serif

Requirements
Must have
• Starting page, product pages, news section, contact, team, services

```html
<!DOCTYPE html>
<html lang="en">
<head>
<meta charset="utf-8">
<title>velbra – Software for every device</title>
<link rel="stylesheet" href="https://fonts.googleapis.com/css2?family=Roboto:wght@300;400;500&family=Nunito+Sans:wght@300;400&display=swap">
<style>
  :root{
    --orange:#f7791f;
    --orange-light:#fb9a33;
    --orange-deep:#fb6a1e;
    --ink:#2f2f33;
    --text:#555;
    --muted:#8a8a8a;
    --line:#e8e8e8;
    --soft-bg:#f6f6f6;
    --white:#fff;
  }
  *{margin:0;padding:0;box-sizing:border-box}
  html,body{width:1200px;height:3550px;overflow:hidden;background:var(--white)}
  body{position:relative;font-family:"Roboto",Arial,sans-serif;color:var(--ink)}
  a{text-decoration:none;color:inherit}
  .abs{position:absolute}
  /* header */
  .brand{left:114px;top:30px;display:flex;align-items:center;gap:10px;font-size:30px;font-weight:500;color:var(--ink);letter-spacing:.5px;line-height:36px}
  .brand-mark{width:16px;height:16px;background:var(--orange)}
  .nav{left:402px;top:33px;display:flex;align-items:center;font-size:13px;color:var(--ink)}
  .nav a{display:block;height:30px;line-height:30px}
  .nav .active{background:var(--orange);color:var(--white);width:62px;text-align:center;border-radius:2px;margin-right:16px}
  .nav .link{margin-right:26px}
  .search{left:889px;top:33px;width:171px;height:30px;border:1px solid #ddd;border-radius:3px;font-size:12px;color:#999;padding:8px 10px;line-height:14px}
  /* hero */
  .hero-wave{left:0;top:0}
  .hero-devices{left:862px;top:172px;width:338px;height:260px;border-radius:14px;background:radial-gradient(ellipse at center,rgba(232,102,26,.22),rgba(232,102,26,0) 70%)}
  .app-card{left:147px;top:189px;width:536px;height:226px;background:var(--white);border-radius:5px;box-shadow:0 10px 30px rgba(0,0,0,.07)}
  .tabs{left:39px;top:26px;width:332px;height:22px;border-bottom:1px solid var(--line);font-size:13px;font-weight:500}
  .tab{position:absolute;top:0}
  .tab-bar{left:0;top:20px;width:74px;height:4px;background:var(--orange);border-radius:2px}
  .card-text{left:35px;top:79px;width:380px;font-size:15.5px;line-height:20px;color:var(--text);font-weight:300}
  .btn{display:block;border:2px solid var(--orange);border-radius:5px;font-size:13px;font-weight:500;color:var(--ink);text-align:center;background:var(--white)}
  .card-btn{left:35px;top:155px;width:212px;height:37px;line-height:33px}
  .hero-title{left:722px;top:240px;color:var(--white);font-size:32px;font-weight:300;line-height:38px}
  .hero-sub{left:722px;top:336px;color:var(--white);font-size:15px;font-weight:300;opacity:.9}
  /* intro */
  .intro{left:0;width:1200px;text-align:center}
  .intro-title{top:540px;font-size:31px;font-weight:300;line-height:39px}
  .intro-text{left:414px;width:386px;top:641px;font-size:16.5px;line-height:20px;color:var(--muted);font-weight:300;text-align:center}
  .intro-link{top:736px;font-size:14px;font-weight:500}
  .photo{overflow:hidden}
  .solutions-photo{top:784px;width:439px;height:259px;border-radius:8px}
  .solution-title{width:439px;text-align:center;font-family:"Nunito Sans",Arial,sans-serif;font-size:33px;font-weight:300;top:1080px}
  .solution-text{width:439px;text-align:center;font-family:"Nunito Sans",Arial,sans-serif;font-size:16px;line-height:25px;color:var(--muted);font-weight:300;top:1128px;padding:0 90px}
  .rule{height:1px;background:var(--line)}
  /* features */
  .feature-band{left:0;top:1885px;width:1200px;height:577px;background:var(--soft-bg)}
  .feature-photo{height:447px;border-radius:0 6px 6px 0}
  .feature-photo.right{border-radius:6px 0 0 6px}
  .feature-title{font-size:38px;font-weight:300;line-height:45px}
  .feature-text{font-size:16px;color:var(--muted);font-weight:300}
  .feature-btn{width:213px;height:37px;line-height:33px}
  /* closing */
  .closing-title{font-size:38px;font-weight:300}
  .closing-text{font-size:16px;color:var(--muted);font-weight:300}
</style>
</head>
<body>

<header>
  <div class="abs brand"><span class="brand-mark"></span>velbra</div>
  <nav class="abs nav">
    <a class="active" href="#">Home</a>
    <a class="link" href="#">Products</a>
    <a class="link" href="#">Services</a>
    <a class="link" href="#">News</a>
    <a class="link" href="#">About</a>
    <a class="link" href="#">Contact</a>
  </nav>
  <div class="abs search">Search...</div>
</header>

<section class="hero">
  <svg class="abs hero-wave" width="1200" height="580" viewBox="0 0 1200 580">
    <defs>
      <linearGradient id="heroGrad" x1="0" y1="0" x2="1" y2="1">
        <stop offset="0" stop-color="#fc9632"/>
        <stop offset="1" stop-color="#fb6b1e"/>
      </linearGradient>
    </defs>
    <path d="M0 165 C 220 100, 430 90, 620 96 C 860 104, 1050 120, 1200 140 L1200 570 C 1000 500, 780 440, 520 425 C 320 414, 130 400, 0 410 Z" fill="url(#heroGrad)"/>
  </svg>
  <div class="abs hero-devices" role="img" aria-label="Faint outline illustration of a laptop, tablet and phone"></div>

  <div class="abs app-card">
    <div class="abs tabs">
      <span class="tab" style="left:21px">App 1</span>
      <span class="tab" style="left:139px">App 2</span>
      <span class="tab" style="left:274px">App 3</span>
      <span class="abs tab-bar"></span>
    </div>
    <p class="abs card-text">Paragraph of text beneath the heading to explain the heading. We'll add onto it with another</p>
    <a class="abs btn card-btn" href="#">Get started with velbra</a>
  </div>

  <h1 class="abs hero-title">Empowering you<br>to make sound decisions.</h1>
  <p class="abs hero-sub">Cross-platform solutions available everywhere</p>
</section>

<section class="solutions">
  <h2 class="abs intro intro-title">No matter who you are,<br>we’ve got what you need.</h2>
  <p class="abs intro-text">Paragraph of text beneath the heading to explain the heading. We'll add onto it with another sen-tence and probably just keep going until we run out of words.</p>
  <a class="abs intro intro-link" href="#">Need a personalized solution&nbsp;&nbsp;&nbsp;&nbsp;→</a>

  <div class="abs photo solutions-photo" style="left:147px;background:linear-gradient(135deg,#e6ecef,#c9d3d8)" role="img" aria-label="Dark paper origami crane hanging against a pale background"></div>
  <div class="abs photo solutions-photo" style="left:615px;background:linear-gradient(135deg,#6f767a,#c4c9cb 60%,#e9eaea)" role="img" aria-label="Man with a tablet standing in a bright office"></div>

  <h3 class="abs solution-title" style="left:142px">Custom Softwares</h3>
  <p class="abs solution-text" style="left:142px">Something short and leading about the collection below—its contents, the creator, etc. Make it short and sweet, but not too short so folks don't simply skip over it entirely.</p>
  <h3 class="abs solution-title" style="left:612px;top:1078px">Consulting</h3>
  <p class="abs solution-text" style="left:612px;top:1126px">Something short and leading about the collection below—its contents, the creator, etc. Make it short and sweet, but not too short so folks don't simply skip over it entirely.</p>

  <div class="abs rule" style="left:136px;top:1320px;width:918px"></div>
</section>

<section class="features">
  <div class="abs photo feature-photo" style="left:0;top:1377px;width:590px;background:linear-gradient(135deg,#3cb394,#2e9a80 55%,#b88a70)" role="img" aria-label="Doctor in green scrubs with stethoscope and wristwatch, arms crossed"></div>
  <h2 class="abs feature-title" style="left:648px;top:1486px">Planning<br>for healthcare organizations</h2>
  <p class="abs feature-text" style="left:650px;top:1594px">Paragraph of text beneath the heading to explain the heading.</p>
  <a class="abs btn feature-btn" href="#" style="left:650px;top:1669px">Read more</a>

  <div class="abs feature-band"></div>
  <div class="abs photo feature-photo right" style="left:619px;top:1946px;width:581px;background:linear-gradient(160deg,#6b5140,#c8cfd2 45%,#8a6a52)" role="img" aria-label="Modern gym with treadmills in front of large windows"></div>
  <h2 class="abs feature-title" style="left:83px;top:2054px">Planning<br>for healthcare organizations</h2>
  <p class="abs feature-text" style="left:86px;top:2162px">Paragraph of text beneath the heading to explain the heading.</p>
  <a class="abs btn feature-btn" href="#" style="left:87px;top:2236px">Read more</a>

  <div class="abs photo feature-photo" style="left:0;top:2520px;width:590px;background:linear-gradient(180deg,#5c6a62,#8a7056 50%,#5e9a3e)" role="img" aria-label="Two deer standing on grass in a forest"></div>
  <h2 class="abs feature-title" style="left:648px;top:2628px">Planning<br>for healthcare organizations</h2>
  <p class="abs feature-text" style="left:650px;top:2736px">Paragraph of text beneath the heading to explain the heading.</p>
  <a class="abs btn feature-btn" href="#" style="left:650px;top:2810px">Read more</a>

  <div class="abs rule" style="left:147px;top:3051px;width:917px"></div>
</section>

<section class="news">
  <h2 class="abs intro closing-title" style="top:3108px">News</h2>
  <p class="abs intro closing-text" style="top:3165px">Paragraph of text beneath the heading to explain the heading.</p>
</section>

<footer>
  <h2 class="abs intro closing-title" style="top:3271px">Footer</h2>
  <p class="abs intro closing-text" style="top:3327px">Paragraph of text beneath the heading to explain the heading.</p>
</footer>

</body>
</html>
```